Used Car Dealer seeks an Amazing Business Card Design

We are looking for a business card design that incorporates our logo and grabs the attention of anyone we give the business card to.

Looking to use the same colors as the logo. Our Logo choice is the black background with Red and Silver/Grey Lettering.

We also would like to see some embossed designs.

Target Market(s)

Used Car Buyers, Automotive, Auto

Industry/Entity Type

Automotive

Contact Information for Business Card

BVEL7K
Gordon Whitlock
482 Tarrow Lane
Suite 207
Roswell, GA 30075
Office (770) 555-0142
Cell (770) 555-0187
bvel7kga@quellmail.com
www.bvel7kga.com

Colors
ffffff
ee3036

Requirements
Must have
• Must include our logo (Black Background with Red and Silver/Grey Lettering)
Nice to have
• Embossed Design. Can be Single or Double Sided.

```html
<!DOCTYPE html>
<html lang="en">
<head>
<meta charset="utf-8">
<title>BVEL7K Business Card</title>
<link href="https://fonts.googleapis.com/css2?family=Open+Sans:wght@400;600&display=swap" rel="stylesheet">
<style>
  :root {
    --canvas: #d9dde2;
    --card-dark: #0b0b0c;
    --card-dark-edge: #2a2a2c;
    --card-light: #eef1f4;
    --brand-red: #ee3036;
    --silver: #b9bcc4;
    --silver-dim: #8d9099;
    --ink: #2b2f36;
    --band: #1c1c1e;
  }
  html, body {
    margin: 0;
    padding: 0;
    width: 1200px;
    height: 1200px;
    overflow: hidden;
    background: var(--canvas);
    font-family: "Open Sans", Arial, sans-serif;
  }
  .canvas { position: relative; width: 1200px; height: 1200px; }

  .card {
    position: absolute;
    width: 840px;
    height: 480px;
    box-shadow: 0 10px 30px rgba(0,0,0,0.25);
    overflow: hidden;
  }

  /* Front */
  .card-front {
    left: 40px; top: 40px;
    background: linear-gradient(160deg, var(--card-dark-edge) 0%, var(--card-dark) 35%, var(--card-dark) 70%, #222 100%);
  }
  .brand-name {
    position: absolute;
    left: 0; right: 0;
    text-align: center;
    font-weight: 600;
    color: var(--brand-red);
    letter-spacing: 2px;
    margin: 0;
  }
  .card-front .brand-name { top: 160px; font-size: 92px; }
  .website {
    position: absolute;
    left: 0; right: 0; top: 348px;
    text-align: center;
    font-size: 26px;
    letter-spacing: 12px;
    color: var(--silver);
    margin: 0;
  }

  /* Back */
  .card-back {
    left: 320px; top: 680px;
    background: linear-gradient(180deg, #f6f8fa 0%, var(--card-light) 60%, #dfe4ea 100%);
    border: 1px solid #cfd4da;
  }
  .card-back .brand-name { top: 92px; font-size: 64px; }
  .name-band {
    position: absolute;
    left: 0; top: 270px;
    width: 360px; height: 66px;
  }
  .name-band svg { position: absolute; inset: 0; }
  .holder-name {
    position: absolute;
    left: 34px; top: 10px;
    margin: 0;
    font-size: 32px;
    font-weight: 400;
    color: var(--silver);
  }
  .contact {
    position: absolute;
    left: 408px; top: 232px;
    color: var(--ink);
    font-size: 16px;
  }
  .address { margin: 0 0 20px; line-height: 22px; }
  .contact-list {
    list-style: none; margin: 0; padding: 0 0 0 16px;
    position: relative;
  }
  .contact-list::before {
    content: ""; position: absolute; left: 28px; top: 0; bottom: 0;
    border-left: 2px solid var(--ink);
  }
  .contact-list li { display: flex; align-items: center; height: 28px; }
  .contact-list svg { width: 20px; height: 18px; margin-right: 28px; margin-left: -16px; }
</style>
</head>
<body>
<main class="canvas">

  <section class="card card-front" aria-label="Business card front">
    <h1 class="brand-name">BVEL7K</h1>
    <p class="website">www.bvel7kga.com</p>
  </section>

  <section class="card card-back" aria-label="Business card back">
    <h2 class="brand-name">BVEL7K</h2>

    <div class="name-band">
      <svg viewBox="0 0 360 66" width="360" height="66" aria-hidden="true">
        <polygon points="0,0 330,0 360,66 0,66" fill="var(--band)"/>
      </svg>
      <p class="holder-name">Gordon Whitlock</p>
    </div>

    <div class="contact">
      <p class="address">482 Tarrow Lane Suite 207 Roswell,<br>GA 30075</p>
      <ul class="contact-list">
        <li>
          <svg viewBox="0 0 20 18" aria-hidden="true"><path d="M4 1 L7 1 L8 5 L6 7 Q8 11 12 12 L14 10 L18 11 L18 14 Q17 17 13 16 Q5 13 2 5 Q2 2 4 1Z" fill="var(--brand-red)"/></svg>
          (770) 555-0187
        </li>
        <li>
          <svg viewBox="0 0 20 18" aria-hidden="true"><rect x="5" y="1" width="10" height="5" fill="var(--brand-red)"/><rect x="1" y="6" width="18" height="8" rx="2" fill="var(--brand-red)"/><rect x="5" y="11" width="10" height="6" fill="#fff" stroke="var(--brand-red)" stroke-width="1.5"/></svg>
          (770) 555-0142
        </li>
        <li>
          <svg viewBox="0 0 20 18" aria-hidden="true"><rect x="1.5" y="3.5" width="17" height="11" fill="none" stroke="var(--brand-red)" stroke-width="1.5"/><polyline points="1.5,3.5 10,10 18.5,3.5" fill="none" stroke="var(--brand-red)" stroke-width="1.5"/></svg>
          bvel7kga@quellmail.com
        </li>
      </ul>
    </div>
  </section>

</main>
</body>
</html>
```